Real Estate "For Sale" Sign for construction company

We need a sign that we can use to hang on a post and place on the road when we sell a property. The sign will be simple and will need to mainly feature our logo (files attached), as well as the words "For Sale", and then our phone number "(555) 617 3489". The sign will hang on a post that'll look something like the attached picture.

Target Market(s)

Home buyers

Industry/Entity Type

Real Estate

Font styles to use
Serif
Sans Serif

Colors
0054AA
0677BA
7BADD7
CADEEF
E8F1F8
0094D4
00A9DD
6FCCEA
C7EBF8
E9F6FB

Requirements
Must have
• For Sale & our phone number

```html
<!DOCTYPE html>
<html lang="en">
<head>
<meta charset="utf-8">
<title>Bluecrest Ridge Homes – For Sale Sign</title>
<link href="https://fonts.googleapis.com/css2?family=Montserrat:wght@500;600&family=Noto+Serif:wght@700&family=Poppins:wght@400&display=swap" rel="stylesheet">
<style>
  :root {
    --page: #ffffff;
    --ink: #111111;
    --sky: #d0e2fb;
    --mist-top: #eceff4;
    --mist-mid: #d3dce6;
    --mist-low: #becddd;
    --brand-blue: #0054aa;
    --navy: #0b1f5c;
    --panel-blue: #6f96d0;
    --white: #ffffff;
    --mark: #7badd7;
  }
  * { margin: 0; padding: 0; box-sizing: border-box; }
  html, body { width: 1034px; height: 1200px; overflow: hidden; background: var(--page); }
  .artboard { position: relative; width: 1034px; height: 1200px; font-family: "Poppins", sans-serif; color: var(--ink); }

  .dimension-label { position: absolute; font-size: 33px; line-height: 1.1; text-align: center; }
  .dimension-label.width { left: 189px; width: 706px; top: 62px; }
  .dimension-label.height { left: 18px; width: 100px; top: 412px; }
  .guides { position: absolute; left: 0; top: 0; }

  .sign { position: absolute; left: 189px; top: 149px; width: 646px; height: 869px; background: var(--panel-blue); overflow: hidden; }

  .brand-band { position: absolute; left: 0; top: 0; width: 100%; height: 332px; background: var(--sky); }
  .brand-mark { position: absolute; left: 273px; top: 88px; width: 100px; height: 100px; border-radius: 50%; background: var(--mark); }
  .brand-name { position: absolute; left: 0; width: 100%; text-align: center; font-family: "Montserrat", sans-serif; font-weight: 500; color: var(--brand-blue); }
  .brand-name.primary { top: 185px; font-size: 52px; letter-spacing: -0.5px; }
  .brand-name.secondary { top: 252px; font-size: 18px; letter-spacing: 15px; padding-left: 15px; }

  .headline-band { position: absolute; left: 0; top: 332px; width: 100%; height: 248px; }
  .mountain-backdrop { position: absolute; inset: 0; background: linear-gradient(180deg, var(--mist-top) 0%, var(--mist-top) 30%, var(--mist-mid) 60%, var(--mist-low) 80%, var(--mist-low) 100%); }
  .headline { position: absolute; left: 0; width: 100%; top: 72px; text-align: center; font-family: "Montserrat", sans-serif; font-weight: 600; font-size: 100px; line-height: 1; color: var(--navy); letter-spacing: 1px; }

  .contact-band { position: absolute; left: 0; top: 580px; width: 100%; height: 214px; background: var(--panel-blue); color: var(--white); text-align: center; font-family: "Noto Serif", serif; font-weight: 700; }
  .call-label { position: absolute; left: 0; width: 100%; top: 42px; font-size: 42px; line-height: 1; }
  .phone { position: absolute; left: 0; width: 100%; top: 104px; font-size: 80px; line-height: 1; letter-spacing: 1px; }

  .web-strip { position: absolute; left: 0; top: 794px; width: 100%; height: 49px; background: var(--brand-blue); color: var(--white); text-align: center; font-family: "Noto Serif", serif; font-weight: 700; font-size: 33px; line-height: 46px; }

  .size-note { position: absolute; left: 0; width: 100%; top: 1066px; text-align: center; font-size: 22px; line-height: 30px; }
</style>
</head>
<body>
<main class="artboard">
  <p class="dimension-label width">18 inch</p>
  <p class="dimension-label height">24<br>inch</p>

  <svg class="guides" width="1034" height="1200" aria-hidden="true">
    <g stroke="#222" stroke-width="1">
      <line x1="189" y1="108" x2="835" y2="108"/>
      <line x1="132" y1="149" x2="132" y2="1018"/>
      <line x1="189" y1="134" x2="189" y2="145"/>
      <line x1="835" y1="134" x2="835" y2="145"/>
      <line x1="172" y1="149" x2="184" y2="149"/>
      <line x1="840" y1="149" x2="852" y2="149"/>
      <line x1="189" y1="1022" x2="189" y2="1033"/>
      <line x1="835" y1="1022" x2="835" y2="1033"/>
      <line x1="172" y1="1018" x2="184" y2="1018"/>
      <line x1="840" y1="1018" x2="852" y2="1018"/>
    </g>
  </svg>

  <section class="sign">
    <header class="brand-band">
      <div class="brand-mark"></div>
      <p class="brand-name primary">Bluecrest Ridge</p>
      <p class="brand-name secondary">HOMES</p>
    </header>

    <div class="headline-band">
      <div class="mountain-backdrop" role="img" aria-label="Soft layered misty mountain range in pale grey-blue"></div>
      <h1 class="headline">FOR SALE</h1>
    </div>

    <div class="contact-band">
      <p class="call-label">CALL:</p>
      <p class="phone">(555) 617 3489</p>
    </div>

    <p class="web-strip">www.yourwebsite.com</p>
  </section>

  <p class="size-note">Size can be adjust as your requirements, Regular<br>Hang on banner size is&nbsp; 18X 24&nbsp; or&nbsp;&nbsp; 24X 18,&nbsp;&nbsp;&nbsp; 24 X 30,&nbsp;&nbsp; 30 X 36 inchs etc.</p>
</main>
</body>
</html>
```